Cat Litter Package and Logo Design

We want new package and Logo design for Cat pine wood litter. Name is “OLVO”. It will be sold in pet store, online shop and supermarket. Our slogan is “Cat litter for your cat, the member of our family”. I mean that cat is not just a pet. They like people in our family. The product for cat is must be the best as selected for member of our family.

Package: Plastic bag with 2 sides
Package Dimension: width 35 cm height 50 cm

Important:
1. Customer will know immediately what product is and for.
2. Outstanding from competitors.
3. Easy to recognize the product.

Front side detail:
1. Cat image
2. Logo: Olvo
3. Slogan: Cat litter for your cat, the member of our family.
4. Detail: Pine Wood Cat Litter
5. Main Highlight -> Breeder Selected
6. Main Features -> Non-Clumping / Odor Control / Dust Free / Save Money / Eco Friendly
7. Show real product (pine wood) inside package: Area to show product will be transparent.
8. Net WT 10 L

Back side detail:
1. One bag for 1 cat & 2 months
2. Benefit: Non-Clumping / Odor Control / Dust Free / Save Money / Eco Friendly
3. How to change for using Olvo Pine Wood Litter: Please mix Olvo with the old one. When your cat can be familiar with Olvo. You can use only Olvo in your cat litter tray.
4. Direction
4.1 Fill the litter height for 2 inches.
4.2 Scoop solid waste.
4.3 Shake litter tray for urine sawdust
4.4 Maintain the height of litter for 2 inches.
5. Imported and Distribution by
5.1 QFO Tech Co.,Ltd.
5.2 Email: Quietfernowlstudio@plumbox.net
6. Little text: *Recommended to use with cat litter tray.

Attached:
1. Our competitors packages
2. Real Cat: You can use it on the package. (I have attached many images, you can select it and use for suitable way.)***
3. Cat litter tray: Don’t use this image. It’s just for describe what is cat litter tray. I prefer drawing.
4. Real product: pine wood

Note: Cat litter is for cat toilet. It's not cat's food.

Target Market(s)

Cat owners whose cats use a litter tray

Industry/Entity Type

Pet

Logo Text

OLVO

Requirements
Must have
• 1. Customer will know immediately what product is and for.
• 2. Outstanding from competitors.
• 3. Easy to recognize the product.

```html
<!DOCTYPE html>
<html lang="en">
<head>
<meta charset="utf-8">
<title>OLVO Pine Wood Cat Litter – Package</title>
<link rel="stylesheet" href="https://fonts.googleapis.com/css2?family=Montserrat:wght@400;500;600;700&family=Roboto+Condensed:ital,wght@0,400;1,700&display=swap">
<style>
  :root{
    --stage:#3b0074;
    --brand:#5e2283;
    --brand-soft:#8a55b0;
    --brand-light:#c9b3dd;
    --cyan:#1db4ea;
    --cyan-deep:#0f9fd6;
    --orange:#f39a2c;
    --yellow:#ffc93c;
    --white:#ffffff;
    --ink:#5e2283;
    --wood-1:#d7a86a;
    --wood-2:#9c6a36;
    --fur-1:#e9c48e;
    --fur-2:#a87a45;
  }
  *{box-sizing:border-box;margin:0;padding:0}
  html,body{width:1200px;height:1200px;overflow:hidden}
  body{background:var(--stage);font-family:"Montserrat",sans-serif;position:relative}

  .panel{position:absolute;top:228px;width:520px;height:743px;overflow:hidden;border-radius:6px}
  .panel--back{left:60px;background:var(--white);color:var(--ink)}
  .panel--front{left:620px;background:var(--cyan);color:var(--white)}

  /* brand mark */
  .brand{position:absolute;display:flex;align-items:center;gap:14px}
  .brand__dot{width:44px;height:44px;border-radius:50%}
  .brand__name{font-family:"Montserrat",sans-serif;font-weight:700;font-size:64px;letter-spacing:4px;line-height:1}
  .panel--back .brand{left:40px;top:48px}
  .panel--back .brand__dot{background:var(--brand)}
  .panel--back .brand__name{color:var(--brand)}
  .panel--front .brand{left:36px;top:64px}
  .panel--front .brand__dot{background:var(--white)}
  .panel--front .brand__name{color:var(--white)}

  .product-name{position:absolute;line-height:1.05}
  .product-name__main{display:block;font-weight:700;font-size:24px}
  .product-name__sub{display:block;font-weight:400;font-size:23px}

  /* ---------- back ---------- */
  .panel--back .product-name{left:150px;top:140px;text-align:right;color:var(--brand)}
  .benefit-icons{position:absolute;right:24px;top:42px;width:200px;display:grid;grid-template-columns:1fr 1fr;row-gap:14px;column-gap:8px}
  .benefit-icons__item{display:flex;flex-direction:column;align-items:center;font-size:9px;font-weight:600;color:var(--brand)}
  .benefit-icons__item:nth-child(3){grid-column:1 / span 2}
  .benefit-icons svg{width:30px;height:30px;margin-bottom:4px}

  .directions{position:absolute;left:40px;top:290px;width:450px;height:250px;border:4px solid var(--brand);border-radius:26px}
  .directions__title{position:absolute;top:-14px;left:110px;background:var(--white);padding:0 14px;font-weight:700;font-size:19px;letter-spacing:1px;color:var(--brand)}
  .directions__steps{list-style:none;display:grid;grid-template-columns:1fr 1fr;gap:40px 24px;padding:56px 24px 0}
  .step{display:flex;align-items:center;gap:12px;font-size:12px;line-height:1.35;color:var(--brand)}
  .step__num{flex:none;width:36px;height:36px;border-radius:50%;background:var(--brand);color:var(--white);display:flex;align-items:center;justify-content:center;font-weight:700;font-size:17px}

  .back-lower{position:absolute;left:0;top:560px;width:100%;height:183px}
  .photo--back-cat{position:absolute;left:40px;top:0;width:140px;height:183px;border-radius:60px 60px 0 0;background:radial-gradient(ellipse at 50% 40%,var(--fur-1),var(--fur-2) 85%)}
  .photo--small-bag{position:absolute;left:196px;top:10px;width:80px;height:120px;border-radius:8px;background:linear-gradient(160deg,var(--brand-light),var(--brand-soft))}
  .switch-note{position:absolute;left:292px;top:6px;width:210px;font-size:10.5px;line-height:1.4;color:var(--brand)}
  .switch-note strong{display:block;font-weight:700;margin-bottom:2px}
  .legal{position:absolute;left:196px;top:140px;font-size:10px;line-height:1.45;color:var(--brand)}
  .legal__note{font-style:italic}

  /* ---------- front ---------- */
  .front-top{position:absolute;left:0;top:0;width:520px;height:330px}
  .panel--front .product-name{right:32px;top:118px;text-align:right;color:var(--white)}
  .slogan{position:absolute;left:36px;top:336px;font-family:"Roboto Condensed",sans-serif;font-size:22px;line-height:1.3;color:var(--white)}
  .window{position:absolute;left:36px;top:402px;width:240px;height:170px;border:5px solid var(--white);border-radius:26px;background:radial-gradient(circle at 30% 30%,var(--wood-1),var(--wood-2) 90%)}
  .photo--front-cat{position:absolute;left:300px;top:300px;width:220px;height:443px;border-radius:110px 40px 0 0;background:radial-gradient(ellipse at 50% 35%,var(--fur-1),var(--fur-2) 80%)}
  .features{position:absolute;left:36px;top:590px;list-style:none}
  .feature{display:flex;align-items:center;gap:12px;height:30px;font-family:"Roboto Condensed",sans-serif;font-style:italic;font-weight:700;font-size:18px;color:var(--white)}
  .feature svg{width:24px;height:24px}
  .net{position:absolute;right:18px;bottom:20px;width:74px;height:74px;border:3px solid var(--white);border-radius:50%;display:flex;flex-direction:column;align-items:center;justify-content:center;background:var(--brand);color:var(--white);line-height:1}
  .net__label{font-size:11px;font-weight:700}
  .net__value{font-size:24px;font-weight:700}
</style>
</head>
<body>

<!-- BACK OF PACK -->
<section class="panel panel--back" aria-label="Back of pack">
  <div class="brand"><span class="brand__dot"></span><span class="brand__name">OLVO</span></div>
  <p class="product-name"><span class="product-name__main">Pine Wood</span><span class="product-name__sub">Cat Litter</span></p>

  <div class="benefit-icons">
    <div class="benefit-icons__item"><svg viewBox="0 0 30 30"><circle cx="15" cy="15" r="15" fill="#5e2283"/><g fill="#fff"><circle cx="11" cy="11" r="2"/><circle cx="19" cy="11" r="2"/><circle cx="15" cy="16" r="2"/><circle cx="11" cy="20" r="2"/><circle cx="19" cy="20" r="2"/></g></svg>Non-Clumping</div>
    <div class="benefit-icons__item"><svg viewBox="0 0 30 30"><circle cx="15" cy="15" r="15" fill="#5e2283"/><path d="M21 15a6 6 0 1 1-2-4.5" fill="none" stroke="#fff" stroke-width="2.5"/><path d="M17 8l3 2.5-3.5 2" fill="none" stroke="#fff" stroke-width="2"/></svg>Odor Control</div>
    <div class="benefit-icons__item"><svg viewBox="0 0 30 30"><circle cx="15" cy="15" r="15" fill="#5e2283"/><text x="15" y="21" text-anchor="middle" font-family="Montserrat,sans-serif" font-weight="700" font-size="17" fill="#fff">$</text></svg>Save Money</div>
    <div class="benefit-icons__item"><svg viewBox="0 0 30 30"><circle cx="15" cy="15" r="15" fill="#5e2283"/><path d="M20 8l-7 9M10 16l5 5-6 2z" fill="#fff" stroke="#fff" stroke-width="2"/></svg>Dust Free</div>
    <div class="benefit-icons__item"><svg viewBox="0 0 30 30"><circle cx="15" cy="15" r="15" fill="#5e2283"/><path d="M15 23s-6-6-6-10a6 6 0 0 1 12 0c0 4-6 10-6 10z" fill="#fff"/><circle cx="15" cy="13" r="2.5" fill="#5e2283"/></svg>Eco Friendly</div>
  </div>

  <div class="directions">
    <h2 class="directions__title">DIRECTIONS</h2>
    <ol class="directions__steps">
      <li class="step"><span class="step__num">1</span>Fill the litter height<br>for 2 inches.</li>
      <li class="step"><span class="step__num">2</span>Scoop solid<br>waste.</li>
      <li class="step"><span class="step__num">3</span>Shake litter tray<br>for urine sawdust.</li>
      <li class="step"><span class="step__num">4</span>Maintain the height of<br>litter for 2 inches.</li>
    </ol>
  </div>

  <div class="back-lower">
    <div class="photo photo--back-cat" role="img" aria-label="Photo of a ginger and white cat standing and looking up"></div>
    <div class="photo photo--small-bag" role="img" aria-label="Illustration of a small purple bag: one bag for one cat, two months"></div>
    <p class="switch-note"><strong>How to change to Olvo Pine Wood Litter</strong>Please mix Olvo with the old one. When your cat can be familiar with Olvo, you can use only Olvo in your cat litter tray.</p>
    <p class="legal">Imported and Distribution by QFO Tech Co.,Ltd.<br>Email: Quietfernowlstudio@plumbox.net<br><span class="legal__note">*Recommended to use with cat litter tray.</span></p>
  </div>
</section>

<!-- FRONT OF PACK -->
<section class="panel panel--front" aria-label="Front of pack">
  <svg class="front-top" viewBox="0 0 520 330" preserveAspectRatio="none" aria-hidden="true">
    <defs>
      <linearGradient id="front-purple" x1="0" y1="0" x2="1" y2="1">
        <stop offset="0" stop-color="#5a1f82"/><stop offset="1" stop-color="#7a2f9a"/>
      </linearGradient>
    </defs>
    <path d="M0 0H520V248C460 262 420 300 360 296C300 292 280 270 220 282C160 294 90 300 0 306Z" fill="url(#front-purple)"/>
    <path d="M0 306C90 300 160 294 220 282C280 270 300 292 360 296C420 300 460 262 520 248" fill="none" stroke="#f39a2c" stroke-width="6"/>
    <path d="M0 313C90 307 160 301 220 289C280 277 300 299 360 303C420 307 460 269 520 255" fill="none" stroke="#ffc93c" stroke-width="4"/>
  </svg>

  <div class="brand"><span class="brand__dot"></span><span class="brand__name">OLVO</span></div>
  <p class="product-name"><span class="product-name__main">Pine Wood</span><span class="product-name__sub">Cat Litter</span></p>

  <p class="slogan">Cat litter for your cat,<br>the member of our family.</p>
  <div class="window" role="img" aria-label="Clear window showing the pine wood pellets inside"></div>
  <div class="photo photo--front-cat" role="img" aria-label="Photo of a ginger and white cat sitting upright"></div>

  <ul class="features">
    <li class="feature"><svg viewBox="0 0 24 24"><circle cx="12" cy="12" r="12" fill="#fff"/><g fill="#1db4ea"><circle cx="9" cy="9" r="1.6"/><circle cx="15" cy="9" r="1.6"/><circle cx="12" cy="13" r="1.6"/><circle cx="9" cy="17" r="1.6"/><circle cx="15" cy="17" r="1.6"/></g></svg>Non-Clumping</li>
    <li class="feature"><svg viewBox="0 0 24 24"><circle cx="12" cy="12" r="12" fill="#fff"/><path d="M17 12a5 5 0 1 1-1.6-3.7" fill="none" stroke="#1db4ea" stroke-width="2.2"/></svg>Odor Control</li>
    <li class="feature"><svg viewBox="0 0 24 24"><circle cx="12" cy="12" r="12" fill="#fff"/><path d="M16 6l-6 7M8 13l4 4-5 2z" fill="#1db4ea" stroke="#1db4ea" stroke-width="1.8"/></svg>Dust Free</li>
    <li class="feature"><svg viewBox="0 0 24 24"><circle cx="12" cy="12" r="12" fill="#fff"/><text x="12" y="17" text-anchor="middle" font-family="Montserrat,sans-serif" font-weight="700" font-size="14" fill="#1db4ea">$</text></svg>Save Money</li>
    <li class="feature"><svg viewBox="0 0 24 24"><circle cx="12" cy="12" r="12" fill="#fff"/><path d="M12 19s-5-5-5-8.5a5 5 0 0 1 10 0C17 14 12 19 12 19z" fill="#1db4ea"/><circle cx="12" cy="10.5" r="2" fill="#fff"/></svg>Eco Friendly</li>
  </ul>

  <div class="net"><span class="net__label">Net WT</span><span class="net__value">10L</span></div>
</section>

</body>
</html>
```